Coupons App Design Project

We have a simple coupons app with few screens and actions:
1. Very simple login screen (with pinloft and zarvik+)
2. Very simple business search page
3. Very simple business search results(each result contains logo icon, business name and delete icon)
4. business list (every row contains logo icon, business name and delete icon)
5. coupons list (each item contains image, title, subtitle, description, expiration time, status graphics (valid, expired, redeemed), delete icon
6. coupon view (image, title, subtitle, description, barcode etc.)
7. custom confirmation dialog(title, buttons, background, text)
8. "scan to subscribe" page (merchant name, merchant number, background image, text, barcode to scan etc.)
9. simple menu
10. splash screen

all graphics should be vector graphics so we can use it to different resolutions including for printing
Updates

Hi all, We've increased the project's budget by 25%. Thanks

Hi all,

We've decided to change the project from refundable to committed payment.
FYI

Hi All,

Thank you for your time and efforts, we really appreciate it.However we've eliminated most of the offered designs we've received becausethey didn't fit our desired look and feel.

Please download our look and feel file from our uploaded files -we've put there some examples of other apps that we like.

Thanks

Brightcart Market(s)

shoppers all over the world

Industry/Entity Type

Business

Requirements
Must have
• Please take a look at the attached file "look & feel.jpg" for some nice screen shots taken from apps that we like

http://www.briefhatchly.com/file.aspx?fileLocation=storage_url/brief_uploads/166833_09lookandfeel_brief010902.jpg
Should not have
• *****************************************************************************************
The attached files are only for demonstration purpose and needs descriptions so please don't send us design based on these screenshots.
*****************************************************************************************

```html
<!DOCTYPE html>
<html lang="en">
<head>
<meta charset="utf-8">
<title>Coupons App – Search Screens</title>
<link rel="stylesheet" href="https://fonts.googleapis.com/css2?family=Roboto:wght@400;500&display=swap">
<style>
:root{
  --stage:#d9d9d9;
  --screen:#e9e9e9;
  --header:#f2844a;
  --accent:#fbae3c;
  --card:#ffffff;
  --divider:#e3e3e3;
  --ink:#222222;
  --ink-soft:#7a7a7a;
  --ink-faint:#8c8c8c;
  --chev:#8a8a8a;
  --white:#ffffff;
  --tile-blue:#1a9ad6;
  --tile-navy:#1c3a55;
  --tile-red:#cc1f3c;
}
*{box-sizing:border-box;margin:0;padding:0}
html,body{width:1200px;height:900px;overflow:hidden}
body{background:radial-gradient(ellipse at 50% 40%,#e2e2e2,var(--stage));font-family:"Roboto",Arial,sans-serif;position:relative}
.screen{position:absolute;top:161px;width:347px;height:579px;background:repeating-linear-gradient(0deg,var(--screen) 0 3px,#e4e4e4 3px 4px);overflow:visible}
.app-bar{position:absolute;left:0;top:0;width:100%;height:38px;background:var(--header)}
.app-bar .back{position:absolute;left:14px;top:10px}
.app-bar .title{position:absolute;left:60px;top:9px;color:var(--white);font-size:18px}
.app-bar .menu{position:absolute;right:12px;top:8px}
.search-bar{position:absolute;left:0;top:38px;width:100%;height:40px;background:var(--accent)}
.search-bar .glass{position:absolute;left:12px;top:11px}
.search-bar .field{position:absolute;left:41px;top:8px;width:291px;height:28px;border-bottom:1px solid rgba(255,255,255,.8);color:#fff6e6;font-size:17px;padding-left:9px;line-height:24px}
.search-bar .clear{position:absolute;left:312px;top:14px}
.list{position:absolute;left:14px;width:318px;background:var(--card);border-radius:4px;overflow:hidden}
.row{position:relative;height:76px;border-bottom:1px solid var(--divider)}
.row:last-child{border-bottom:0}
.row.active{background:var(--accent)}
.tile{position:absolute;left:9px;top:8px;width:59px;height:59px;border:1px solid #dcdcdc;background:var(--white);display:flex;align-items:center;justify-content:center;font-size:11px;font-weight:500;color:var(--ink)}
.tile.blue{background:var(--tile-blue);color:var(--white);border-color:var(--tile-blue)}
.tile.navy{background:var(--tile-navy);color:var(--white);border-color:var(--tile-navy)}
.tile.red{color:var(--tile-red)}
.name{position:absolute;left:92px;top:13px;font-size:17px;font-weight:500;color:var(--ink)}
.sub{position:absolute;left:92px;top:33px;font-size:13px;color:var(--ink-soft)}
.info{position:absolute;left:92px;top:51px;font-size:10.5px;color:var(--ink-faint)}
.row.active .name,.row.active .sub,.row.active .info{color:var(--white)}
.chev{position:absolute;right:14px;top:28px}
.dropdown{position:absolute;left:167px;top:44px;width:174px;background:var(--accent);box-shadow:0 2px 4px rgba(0,0,0,.2)}
.dropdown::before{content:"";position:absolute;right:16px;top:-7px;border:7px solid transparent;border-top:0;border-bottom-color:var(--accent)}
.menu-item{height:36px;display:flex;align-items:center;gap:12px;padding-left:10px;color:var(--white);font-size:17px;font-weight:500;border-bottom:1px solid rgba(255,255,255,.45)}
.menu-item:last-child{border-bottom:0}
.zoom{position:absolute;left:284px;top:633px;width:152px;height:152px;border-radius:50%;border:2px solid #6f6f6f;background:#e6e6e6;overflow:hidden}
.zoom .label{position:absolute;width:100%;top:128px;text-align:center;font-size:11px;color:#333}
</style>
</head>
<body>

<!-- Screen 1: search -->
<section class="screen" style="left:40px">
  <header class="app-bar">
    <svg class="back" width="12" height="18" viewBox="0 0 12 18"><polyline points="10,2 3,9 10,16" fill="none" stroke="#fff" stroke-width="2.6"/></svg>
    <span class="title">Search</span>
    <svg class="menu" width="26" height="22" viewBox="0 0 26 22"><rect y="0" width="26" height="6" rx="1" fill="#fff"/><rect y="8" width="26" height="6" rx="1" fill="#fff"/><rect y="16" width="26" height="6" rx="1" fill="#fff"/></svg>
  </header>
  <div class="search-bar">
    <svg class="glass" width="20" height="20" viewBox="0 0 20 20"><circle cx="8" cy="8" r="6" fill="none" stroke="#fff" stroke-width="2.6"/><line x1="12.5" y1="12.5" x2="18" y2="18" stroke="#fff" stroke-width="3" stroke-linecap="round"/></svg>
    <div class="field">Search</div>
    <svg class="clear" width="14" height="14" viewBox="0 0 14 14"><path d="M1 1L13 13M13 1L1 13" stroke="#fff" stroke-width="1.8"/></svg>
  </div>
  <div class="list" style="top:87px">
    <div class="row"><div class="tile">Norvella</div><div class="name">Norvella</div><div class="sub">Great Local Deals In Your City</div><div class="info">Some infomation</div><svg class="chev" width="12" height="20" viewBox="0 0 12 20"><polyline points="2,2 10,10 2,18" fill="none" stroke="#8a8a8a" stroke-width="2.4"/></svg></div>
    <div class="row"><div class="tile red">Brightcart</div><div class="name">Brightcart</div><div class="sub">Great Local Deals</div><div class="info">Some infomation</div><svg class="chev" width="12" height="20" viewBox="0 0 12 20"><polyline points="2,2 10,10 2,18" fill="none" stroke="#8a8a8a" stroke-width="2.4"/></svg></div>
    <div class="row"><div class="tile blue">Kestrel</div><div class="name">Kestrel</div><div class="sub">Built to go further</div><div class="info">Some infomation</div><svg class="chev" width="12" height="20" viewBox="0 0 12 20"><polyline points="2,2 10,10 2,18" fill="none" stroke="#8a8a8a" stroke-width="2.4"/></svg></div>
    <div class="row"><div class="tile">Tradlo</div><div class="name">Tradlo</div><div class="sub">Shop it, swap it, keep it</div><div class="info">Some infomation</div><svg class="chev" width="12" height="20" viewBox="0 0 12 20"><polyline points="2,2 10,10 2,18" fill="none" stroke="#8a8a8a" stroke-width="2.4"/></svg></div>
  </div>
</section>

<!-- Screen 2: menu open -->
<section class="screen" style="left:427px">
  <header class="app-bar">
    <svg class="back" width="12" height="18" viewBox="0 0 12 18"><polyline points="10,2 3,9 10,16" fill="none" stroke="#fff" stroke-width="2.6"/></svg>
    <span class="title">Search</span>
    <svg class="menu" width="26" height="22" viewBox="0 0 26 22"><rect y="0" width="26" height="6" rx="1" fill="#fff"/><rect y="8" width="26" height="6" rx="1" fill="#fff"/><rect y="16" width="26" height="6" rx="1" fill="#fff"/></svg>
  </header>
  <div class="list" style="top:38px;border-radius:0 0 4px 4px">
    <div class="row"><div class="tile">Norvella</div><div class="name">Norvella</div><div class="sub">Great Local Deals In Your City</div><div class="info">Some infomation</div></div>
    <div class="row"><div class="tile red">Brightcart</div><div class="name">Brightcart</div><div class="sub">Great Local Deals</div><div class="info">Some infomation</div><svg class="chev" width="12" height="20" viewBox="0 0 12 20"><polyline points="2,2 10,10 2,18" fill="none" stroke="#8a8a8a" stroke-width="2.4"/></svg></div>
    <div class="row"><div class="tile blue">Kestrel</div><div class="name">Kestrel</div><div class="sub">Built to go further</div><div class="info">Some infomation</div></div>
    <div class="row"><div class="tile">Tradlo</div><div class="name">Tradlo</div><div class="sub">Shop it, swap it, keep it</div><div class="info">Some infomation</div><svg class="chev" width="12" height="20" viewBox="0 0 12 20"><polyline points="2,2 10,10 2,18" fill="none" stroke="#8a8a8a" stroke-width="2.4"/></svg></div>
    <div class="row"><div class="tile red">Lumio</div><div class="name">Lumio</div><div class="sub">Live Bright</div><div class="info">Some infomation</div><svg class="chev" width="12" height="20" viewBox="0 0 12 20"><polyline points="2,2 10,10 2,18" fill="none" stroke="#8a8a8a" stroke-width="2.4"/></svg></div>
    <div class="row"><div class="tile navy">Vantix</div><div class="name">Vantix</div><div class="sub">Business Sub Title</div><div class="info">Some infomation</div><svg class="chev" width="12" height="20" viewBox="0 0 12 20"><polyline points="2,2 10,10 2,18" fill="none" stroke="#8a8a8a" stroke-width="2.4"/></svg></div>
  </div>
  <nav class="dropdown">
    <div class="menu-item"><svg width="20" height="18" viewBox="0 0 20 18"><path d="M10 17L2 9A4.6 4.6 0 0 1 10 3A4.6 4.6 0 0 1 18 9Z" fill="#fff"/></svg>Favorite</div>
    <div class="menu-item"><svg width="20" height="20" viewBox="0 0 20 20"><path d="M9 2H18V11L10 19L1 10Z" fill="#fff"/><circle cx="14" cy="6" r="1.6" fill="#fbae3c"/></svg>My coupons</div>
    <div class="menu-item"><svg width="20" height="20" viewBox="0 0 20 20"><circle cx="6" cy="6" r="5" fill="#fff"/><path d="M9 9L18 18M14 14L16 12M16 16L18 14" stroke="#fff" stroke-width="2.6"/></svg>Log out</div>
  </nav>
</section>

<!-- Screen 3: row selected -->
<section class="screen" style="left:814px">
  <header class="app-bar">
    <svg class="back" width="12" height="18" viewBox="0 0 12 18"><polyline points="10,2 3,9 10,16" fill="none" stroke="#fff" stroke-width="2.6"/></svg>
    <span class="title">Search</span>
    <svg class="menu" width="26" height="22" viewBox="0 0 26 22"><rect y="0" width="26" height="6" rx="1" fill="#fff"/><rect y="8" width="26" height="6" rx="1" fill="#fff"/><rect y="16" width="26" height="6" rx="1" fill="#fff"/></svg>
  </header>
  <div class="list" style="top:38px;border-radius:0 0 4px 4px">
    <div class="row"><div class="tile">Norvella</div><div class="name">Norvella</div><div class="sub">Great Local Deals In Your City</div><div class="info">Some infomation</div><svg class="chev" width="12" height="20" viewBox="0 0 12 20"><polyline points="2,2 10,10 2,18" fill="none" stroke="#8a8a8a" stroke-width="2.4"/></svg></div>
    <div class="row"><div class="tile red">Brightcart</div><div class="name">Brightcart</div><div class="sub">Great Local Deals</div><div class="info">Some infomation</div><svg class="chev" width="12" height="20" viewBox="0 0 12 20"><polyline points="2,2 10,10 2,18" fill="none" stroke="#8a8a8a" stroke-width="2.4"/></svg></div>
    <div class="row active"><div class="tile blue">Kestrel</div><div class="name">Kestrel</div><div class="sub">Built to go further</div><div class="info">Some infomation</div><svg class="chev" width="12" height="20" viewBox="0 0 12 20"><polyline points="2,2 10,10 2,18" fill="none" stroke="#fff" stroke-width="2.6"/></svg></div>
    <div class="row"><div class="tile">Tradlo</div><div class="name">Tradlo</div><div class="sub">Shop it, swap it, keep it</div><div class="info">Some infomation</div><svg class="chev" width="12" height="20" viewBox="0 0 12 20"><polyline points="2,2 10,10 2,18" fill="none" stroke="#8a8a8a" stroke-width="2.4"/></svg></div>
    <div class="row"><div class="tile red">Lumio</div><div class="name">Lumio</div><div class="sub">Live Bright</div><div class="info">Some infomation</div><svg class="chev" width="12" height="20" viewBox="0 0 12 20"><polyline points="2,2 10,10 2,18" fill="none" stroke="#8a8a8a" stroke-width="2.4"/></svg></div>
    <div class="row"><div class="tile navy">Vantix</div><div class="name">Vantix</div><div class="sub">Business Sub Title</div><div class="info">Some infomation</div><svg class="chev" width="12" height="20" viewBox="0 0 12 20"><polyline points="2,2 10,10 2,18" fill="none" stroke="#8a8a8a" stroke-width="2.4"/></svg></div>
  </div>
</section>

<!-- Texture detail callout -->
<div class="zoom">
  <svg width="152" height="152" viewBox="0 0 152 152">
    <rect x="0" y="0" width="104" height="152" fill="#e9e9e9"/>
    <path d="M104 0V90A30 30 0 0 0 134 120H152V0Z" fill="#ffffff"/>
    <path d="M104 0V90A30 30 0 0 0 134 120" fill="none" stroke="#dadada" stroke-width="1"/>
    <g stroke="#c9c9c9" stroke-width="3">
      <line x1="40" y1="10" x2="70" y2="10"/><line x1="85" y1="10" x2="104" y2="10"/>
      <line x1="20" y1="34" x2="50" y2="34"/><line x1="66" y1="34" x2="96" y2="34"/>
      <line x1="30" y1="58" x2="60" y2="58"/><line x1="76" y1="58" x2="104" y2="58"/>
      <line x1="10" y1="82" x2="40" y2="82"/><line x1="56" y1="82" x2="86" y2="82"/>
      <line x1="28" y1="106" x2="58" y2="106"/><line x1="74" y1="106" x2="104" y2="106"/>
    </g>
  </svg>
  <div class="label">Zoom 800%</div>
</div>

</body>
</html>
```